Fable Organics Label Project- Updates made to project!

Project Scope: Branding opportunity for internet based skin care line. Design coordinating label for 4 different products. Each design shall be editable in Adobe Illustrator as a template including all fonts, symbols, and guides. Submit a design for all 4 products (preferably together as it would look on a retail shelf), business card, and logo.
Cleanser: STEP 1 Label Size: 5 x 4.5 inches (w x h) LULL CLEANSER
Toner: STEP 2 Label Size: 5 x 4.5 inches (w x h) HUSHWAY TONER- A piece of each crystal sits at the bottom of each solution. It coordinates with the "Calm Within" of our logo.
Serum STEP 3 Label Size: Label Size: 4.25 x 2.25 ANTI-AGING SERUM
Moisturizer: STEP 4 Label Size: Label Size: 1”x7.25” MOISTURIZER
Each label needs to include:
Front:
Attractive larger sized STEP #
Logo
Product name and short description
Decorative design Symbol(s)
Back:
Area on back to say short description
Directions for use
Larger area for ingredients
Website: www.fableorganics-example.com
Address of distribution
Barcode

Fable Skin Care, an esthetician created line provides organic and natural based products for all skin types. With an emphasis on anti-aging, this simple 4- step system can be used by many including pregnant and oncology consumers. The unique thing about our line is that the toners and serums contain crystals such as amethyst and rose quarts to promote inner peace as well as outer beauty. Each product is handmade with natural, quality ingredients and are 70-90% Organic.
Target Market: Women ages 30-45 years old. This demographic is on the go, and wants a simple-easy to read label, & a skin care system that addresses her concerns. Just as this consumer is mindful of her fitness and what she puts in her body, she tends to purchase environmentally friendly, and natural products. Health and wellness trends reflect this, as organic beauty products are expected to grow 74% from 2013 to 2018. She enjoys meditation and yoga, and she is curious about eastern medicine holistic healing trends.

Company Name: Fable Skin Care
Tagline: Calm Within- Glow Without
Package Feel: Simple, elegant easy to read step on each product. STEP 1: AM/PM. Attractive numbering. A symbol that reflects the brand. Not necessarily a Fable or Crystal because the name speaks for itself. Beautiful, soft, eye catching design that draws the consumer to pick it up. Clear or white label welcomed. Some color palettes provided.
Descriptive words the packaging should represent: Yoga, Zen, mystic, eye catching, healing energy, natural, quality ingredients, sophisticated, beautiful, serenity, easy to read- bold-attractive numbering on front.
Inspiration Brands: KAVU Organics- Beautiful watercolor packaging that resonates a "feeling"

Attached are pictures of the packaging, inspirational pictures, skin care lines that are attractive, ect.

Packaging SPECS:

Cleanser:
Color Clear
Size 4 oz
Material PET
Case Pack
Neck Finish 24-410
Diameter 1.58 in / 4.013 cm
Height 6 in / 15.240 cm
Label Dimensions 5x4.5
Print Dimensions 5x4.5
Print Dimensions in (diameter)

TONER BOTTLE: Same as above

SERUM BOTTLE:
Color Clear
Size 2 oz
Material PET
Neck Finish 20-410
Diameter 1.358 in / 3.449 cm
Height 3.274 in / 8.316 cm

Moisturizer:
2.3 oz
Height:53 mm
Diameter: 60 mm
Neck: 58/400

Target Market(s)

Women ages 30-45 years old. This demographic is on the go, and wants a simple-easy to read label, & a skin care system that addresses her concerns. Just as this consumer is mindful of her fitness and what she puts in her body, she tends to purchase environmentally friendly, and natural products. Health and wellness trends reflect this, as organic beauty products are expected to grow 74% from 2013 to 2018. She enjoys meditation and yoga, and she is curious about eastern medicine holistic healing trends.

Industry/Entity Type

Skin Care Product

Contact Information for Business Card

Details given upon completion.

Logo Text

Fable Organics Calm Within- Glow Without

Requirements
Must have
• A large step number on the front. Coordinating symbols and colors. Must have a professional retail look and be easy to read.
Nice to have
• Clean, simple, eye catching packaging. Watercolor designs. Designs that inspire "feelings" www.kavuorganics-example.com

```html
<!DOCTYPE html>
<html lang="en">
<head>
<meta charset="utf-8">
<title>Fable Skin Care – Label Set</title>
<link rel="stylesheet" href="https://fonts.googleapis.com/css2?family=EB+Garamond:wght@400;500&family=Bodoni+Moda:wght@500&display=swap">
<style>
  :root {
    --backdrop: #efede9;
    --label-paper: #f8f7f4;
    --label-ink: #2a2a2c;
    --label-light: #ffffff;
  }
  html, body { margin: 0; padding: 0; overflow: hidden; }
  .canvas {
    position: relative;
    width: 1200px;
    height: 1000px;
    background: var(--backdrop);
    overflow: hidden;
    font-family: "EB Garamond", Georgia, serif;
  }
  .label {
    position: absolute;
    background: var(--label-paper);
    overflow: hidden;
  }
  .label svg { position: absolute; left: 0; top: 0; }
  .band { fill: var(--label-ink); }
  .step-number {
    font-family: "Bodoni Moda", "Didot", serif;
    font-weight: 500;
    text-anchor: middle;
  }
  .step-number.on-paper { fill: var(--label-ink); }
  .step-number.on-band { fill: var(--label-light); }
  .brand {
    position: absolute;
    font-family: "EB Garamond", Georgia, serif;
    font-weight: 400;
    color: var(--label-ink);
    line-height: 1;
    margin: 0;
  }
  .divider {
    position: absolute;
    width: 1px;
    background: var(--label-ink);
  }
  .skincare {
    position: absolute;
    writing-mode: vertical-rl;
    font-family: "EB Garamond", Georgia, serif;
    color: var(--label-ink);
    letter-spacing: 0.3em;
    line-height: 1;
    text-transform: uppercase;
    margin: 0;
  }
  .product-name {
    position: absolute;
    color: var(--label-light);
    text-transform: uppercase;
    text-align: center;
    letter-spacing: 0.02em;
    line-height: 1.1;
    margin: 0;
  }
  .product-copy {
    position: absolute;
    color: var(--label-light);
    text-align: center;
    line-height: 1.25;
    margin: 0;
  }

  /* Step 2 – toner */
  .label-toner { left: 105px; top: 478px; width: 263px; height: 279px; }
  .label-toner .brand { left: 14px; top: 22px; font-size: 70px; }
  .label-toner .divider { left: 226px; top: 10px; height: 140px; }
  .label-toner .skincare { left: 240px; top: 30px; font-size: 9px; }
  .label-toner .product-name { left: 0; width: 263px; top: 226px; font-size: 13px; }
  .label-toner .product-copy { left: 10px; width: 243px; top: 244px; font-size: 9px; }

  /* Step 1 – cleanser */
  .label-cleanser { left: 441px; top: 467px; width: 185px; height: 198px; }
  .label-cleanser .brand { left: 8px; top: 12px; font-size: 44px; }
  .label-cleanser .divider { left: 160px; top: 6px; height: 96px; }
  .label-cleanser .skincare { left: 168px; top: 18px; font-size: 6.5px; }
  .label-cleanser .product-name { left: 0; width: 150px; top: 154px; font-size: 9px; }
  .label-cleanser .product-copy { left: 6px; width: 173px; top: 167px; font-size: 6.5px; }

  /* Step 3 – serum */
  .label-serum { left: 653px; top: 562px; width: 157px; height: 143px; }
  .label-serum .brand { left: 26px; top: 12px; font-size: 34px; }
  .label-serum .divider { left: 130px; top: 6px; height: 68px; }
  .label-serum .skincare { left: 137px; top: 12px; font-size: 5.5px; }
  .label-serum .product-name { left: 0; width: 157px; top: 116px; font-size: 6.5px; }
  .label-serum .product-copy { left: 8px; width: 141px; top: 125px; font-size: 5.5px; }

  /* Step 4 – moisturizer */
  .label-moisturizer { left: 838px; top: 662px; width: 305px; height: 192px; }
  .label-moisturizer .brand { left: 76px; top: 18px; font-size: 50px; }
  .label-moisturizer .divider { left: 228px; top: 8px; height: 74px; }
  .label-moisturizer .skincare { left: 238px; top: 14px; font-size: 7.5px; }
  .label-moisturizer .product-name { left: 0; width: 305px; top: 154px; font-size: 10px; }
  .label-moisturizer .product-copy { left: 70px; width: 165px; top: 167px; font-size: 6.5px; }
</style>
</head>
<body>
<main class="canvas">

  <section class="label label-toner">
    <svg width="263" height="279" viewBox="0 0 263 279">
      <defs>
        <clipPath id="toner-paper"><path d="M0 0 H263 V157 C180 168 100 195 0 202 Z"/></clipPath>
        <clipPath id="toner-band"><path d="M0 202 C100 195 180 168 263 157 V279 H0 Z"/></clipPath>
      </defs>
      <path class="band" d="M0 202 C100 195 180 168 263 157 V279 H0 Z"/>
      <text class="step-number on-paper" x="124" y="218" font-size="110" clip-path="url(#toner-paper)">2</text>
      <text class="step-number on-band" x="124" y="218" font-size="110" clip-path="url(#toner-band)">2</text>
    </svg>
    <p class="brand">Fable</p>
    <span class="divider"></span>
    <p class="skincare">Skincare</p>
    <h2 class="product-name">Hushway Toner</h2>
    <p class="product-copy">Gentle mist of rose water and quartz essence that balances, softens and readies skin for serum. Spray on clean face, morning and night.</p>
  </section>

  <section class="label label-cleanser">
    <svg width="185" height="198" viewBox="0 0 185 198">
      <defs>
        <clipPath id="cleanser-paper"><path d="M0 0 H185 V108 C120 116 60 134 0 140 Z"/></clipPath>
        <clipPath id="cleanser-band"><path d="M0 140 C60 134 120 116 185 108 V198 H0 Z"/></clipPath>
      </defs>
      <path class="band" d="M0 140 C60 134 120 116 185 108 V198 H0 Z"/>
      <text class="step-number on-paper" x="76" y="150" font-size="72" clip-path="url(#cleanser-paper)">1</text>
      <text class="step-number on-band" x="76" y="150" font-size="72" clip-path="url(#cleanser-band)">1</text>
    </svg>
    <p class="brand">Fable</p>
    <span class="divider"></span>
    <p class="skincare">Skincare</p>
    <h2 class="product-name">Lull Cleanser</h2>
    <p class="product-copy">Soft foaming wash with green tea and aloe that lifts away the day without stripping. Massage onto damp skin, rinse well.</p>
  </section>

  <section class="label label-serum">
    <svg width="157" height="143" viewBox="0 0 157 143">
      <defs>
        <clipPath id="serum-paper"><path d="M0 0 H157 V78 C110 86 60 106 0 113 Z"/></clipPath>
        <clipPath id="serum-band"><path d="M0 113 C60 106 110 86 157 78 V143 H0 Z"/></clipPath>
      </defs>
      <path class="band" d="M0 113 C60 106 110 86 157 78 V143 H0 Z"/>
      <text class="step-number on-paper" x="82" y="113" font-size="56" clip-path="url(#serum-paper)">3</text>
      <text class="step-number on-band" x="82" y="113" font-size="56" clip-path="url(#serum-band)">3</text>
    </svg>
    <p class="brand">Fable</p>
    <span class="divider"></span>
    <p class="skincare">Skincare</p>
    <h2 class="product-name">Anti-Aging Serum</h2>
    <p class="product-copy">Light amethyst serum with vitamin C to firm and brighten. Press three drops into skin.</p>
  </section>

  <section class="label label-moisturizer">
    <svg width="305" height="192" viewBox="0 0 305 192">
      <defs>
        <clipPath id="moisturizer-paper"><path d="M0 0 H305 V86 C200 94 100 112 0 120 Z"/></clipPath>
        <clipPath id="moisturizer-band"><path d="M0 120 C100 112 200 94 305 86 V192 H0 Z"/></clipPath>
      </defs>
      <path class="band" d="M0 120 C100 112 200 94 305 86 V192 H0 Z"/>
      <text class="step-number on-paper" x="176" y="148" font-size="66" clip-path="url(#moisturizer-paper)">4</text>
      <text class="step-number on-band" x="176" y="148" font-size="66" clip-path="url(#moisturizer-band)">4</text>
    </svg>
    <p class="brand">Fable</p>
    <span class="divider"></span>
    <p class="skincare">Skincare</p>
    <h2 class="product-name">Moisturizer</h2>
    <p class="product-copy">Rich whipped cream of shea and jojoba that locks in moisture for a calm, even glow. Smooth over face and neck daily.</p>
  </section>

</main>
</body>
</html>
```